A professional business to business web site for a contract agency called VANTOMER.

We need a very clean, very professional web site created for business to business. It is an informational web site with 3 pages. We are a company that offers contract employee placements into primarily the pharmaceutical industry. I have attached a file that describes the company more fully.
Updates

Hi,

I'm sorry if I wasn't clear, but I need to have the HTML pages created so I can just upload the files you give me to the web hosting site.

Please let me know if you have any questions.

Thanks for working on my project!

Hello,

I didn't put this in the description, but I would need the web site set up on the web hosting site as well.  The web hosting site is bluepinecrest.  I want a copy of all the files as well.

Thanks,
Milo

Reason: I'm sorry, unexpectedly, I have been very busy and I haven't been able to devote the time necessary for this. I am extending the deadline by 10 days. Thank you for your patience. Thanks.

Reason: Hi everyone, I apologize again, but everything has been so busy here that I haven't been able to give this attention. I plan to work on this over the next few days. Thanks and sorry again, Milo.

Reason: I'm sorry this is taking longer than planned. I have been extremely busy. I have increased the budget on this project. Thanks.

Target Market(s)

Large professional corporations mainly in the pharmaceutical industry. The audience is hiring decisions makers within the companies and potential job candidates/job seekers.

Industry/Entity Type

Pharmaceutical

Font styles to use
Sans Serif

Requirements
Must have
• Must have a clean look that mimics the pharmaceutical industry web sites. VERY professional.
Nice to have
• A nice picture of professional business/pharma/technical people looking like a team. Colors are listed on the attached Word document.
Should not have
• No animation. Not too busy.

```html
<!DOCTYPE html>
<html lang="en">
<head>
<meta charset="utf-8">
<title>VANTOMER – Contract Professionals</title>
<link href="https://fonts.googleapis.com/css2?family=Montserrat:wght@400;600;700;800&family=Raleway:wght@300;400;500;600;700&display=swap" rel="stylesheet">
<style>
:root{
  --teal:#1fb497;
  --teal-dark:#17957d;
  --navy:#0f4a6a;
  --ink:#222;
  --text:#555;
  --muted:#8a8a8a;
  --light:#eeeeee;
  --white:#fff;
}
*{box-sizing:border-box;margin:0;padding:0}
html,body{width:1200px;height:3112px;overflow:hidden}
body{position:relative;background:var(--white);font-family:'Raleway',sans-serif;color:var(--text)}
.abs{position:absolute}

/* header */
.site-header{left:0;top:0;width:1200px;height:88px;background:linear-gradient(#0b3f4a,#14505c);z-index:3}
.brand{left:98px;top:22px;display:flex;align-items:center;gap:12px}
.brand-dot{width:40px;height:40px;border-radius:50%;background:var(--teal)}
.brand-name{font-family:'Montserrat',sans-serif;font-weight:700;font-size:28px;letter-spacing:2px;color:var(--white)}
.top-contact{right:98px;top:8px;font-size:11px;color:var(--white);display:flex;gap:18px;align-items:center}
.top-contact svg{vertical-align:-2px;margin-right:4px}
.main-nav{right:98px;top:44px;display:flex;gap:8px}
.main-nav a{font-family:'Montserrat',sans-serif;font-size:12px;font-weight:600;color:var(--white);text-decoration:none;border:2px solid var(--teal);border-radius:16px;padding:6px 16px}
.main-nav a.active{background:var(--teal)}

/* hero */
.hero{left:0;top:88px;width:1200px;height:477px;background:linear-gradient(100deg,#34444f 0%,#6f8290 40%,#c9d3da 75%,#e8edf0 100%)}
.hero-copy{left:98px;top:95px;width:560px;color:var(--white)}
.hero-title{font-family:'Montserrat',sans-serif;font-weight:800;font-size:54px;line-height:58px;text-transform:uppercase}
.hero-text{margin-top:22px;font-size:13px;line-height:18px;text-transform:uppercase;width:430px}
.hero-actions{margin-top:22px;display:flex;gap:22px}
.btn{font-family:'Montserrat',sans-serif;font-weight:600;font-size:15px;border-radius:24px;padding:11px 28px;color:var(--white);text-decoration:none;border:3px solid var(--white)}
.btn.teal{border-color:var(--teal);padding:11px 48px}
.hero-notch{left:540px;top:520px;width:120px;height:46px}

/* clients */
.clients{left:0;top:565px;width:1200px;height:147px;background:var(--light)}
.client-row{left:170px;top:40px;width:860px;display:flex;justify-content:space-between;align-items:center;height:50px;color:#333}
.client-name{font-family:'Raleway',sans-serif;font-weight:600;font-size:20px}
.client-badge{width:36px;height:40px;background:#bdbdbd;border-radius:4px}
.clients-tab{left:540px;top:115px;width:120px;height:32px;background:var(--navy);color:var(--white);font-family:'Montserrat',sans-serif;font-weight:600;font-size:12px;display:flex;align-items:center;justify-content:center}

/* section headings */
.section-title{left:0;width:1200px;text-align:center;font-family:'Montserrat',sans-serif;font-weight:700;font-size:48px;color:#111}
.section-lede{left:150px;width:900px;text-align:center;font-size:12px;line-height:17px;text-transform:uppercase;color:var(--muted)}

/* services */
.service{top:935px;width:331px}
.service-photo{height:205px}
.service-title{margin-top:22px;text-align:center;font-size:27px;color:#222}
.service-text{margin:10px auto 0;width:280px;text-align:center;font-size:11px;line-height:15px;color:var(--muted)}

/* updates */
.updates{left:0;top:1323px;width:1200px;height:547px;background:var(--light)}
.updates-sub{left:0;width:1200px;text-align:center;font-family:'Montserrat',sans-serif;font-size:15px;letter-spacing:5px;color:var(--teal);text-transform:uppercase;line-height:30px}
.update-lead{left:210px;top:208px;width:360px;text-align:right}
.update-tag{font-family:'Montserrat',sans-serif;font-weight:700;font-size:17px;color:var(--teal)}
.update-big{margin-top:22px;font-size:27px;line-height:38px;font-weight:300;color:#777}
.update-rule{left:598px;top:205px;width:1px;height:285px;background:#d2d2d2}
.update-body{left:625px;top:205px;width:370px;font-size:12px;line-height:18px;color:var(--muted)}
.update-body .intro{color:#333;font-weight:500;margin-bottom:18px}
.update-body p+p{margin-top:16px}
.arrow{top:290px}

/* contact intro */
.quote-mark{left:98px;top:2060px;font-family:'Montserrat',sans-serif;font-weight:800;font-size:130px;line-height:130px;color:var(--teal)}
.quote{left:250px;top:2078px;width:300px;text-align:center;font-size:20px;line-height:27px;color:#333}
.quote-cite{display:block;margin-top:16px;font-size:15px;color:var(--muted)}
.pitch{left:605px;top:2072px;width:400px;color:#222}
.pitch h3{font-weight:400;font-size:18px;line-height:24px}
.pitch h4{font-weight:700;font-size:18px;line-height:24px}
.pitch p{margin-top:18px;font-size:12px;line-height:17px;color:#444}
.pitch b{color:#111}

.divider{left:98px;top:2400px;width:1004px;height:1px;background:#e2e2e2}
.contact-item{top:2437px;font-size:12px;color:#333}
.contact-item strong{display:block;margin-top:6px;font-family:'Montserrat',sans-serif;font-size:19px;color:#111}
.contact-brand{left:470px;top:2430px;display:flex;align-items:center;gap:12px}
.contact-brand .brand-name{color:var(--teal)}

/* map */
.map{left:98px;top:2517px;width:1004px;height:380px;background:linear-gradient(135deg,#e7e9ea,#d4d9dc)}
.map-card{left:197px;top:2590px;width:210px;height:210px;border-radius:50%;background:var(--white);box-shadow:0 2px 10px rgba(0,0,0,.15);text-align:center;padding-top:46px;font-size:11px;line-height:15px;color:#333}
.map-card h5{font-family:'Montserrat',sans-serif;font-size:15px;margin-bottom:10px;color:#111}

/* footer */
.site-footer{left:0;top:2925px;width:1200px;text-align:center;font-size:12px;line-height:18px;color:#666;text-transform:uppercase}
.footer-band{left:0;top:3023px;width:1200px;height:89px;background:var(--navy)}
.to-top{left:565px;top:2988px;width:70px;height:70px;border-radius:50%;background:var(--teal);display:flex;align-items:center;justify-content:center}
</style>
</head>
<body>

<header class="site-header abs">
  <div class="brand abs"><span class="brand-dot"></span><span class="brand-name">VANTOMER</span></div>
  <div class="top-contact abs">
    <span><svg width="11" height="11" viewBox="0 0 24 24"><path fill="#fff" d="M6.6 10.8a15 15 0 0 0 6.6 6.6l2.2-2.2a1 1 0 0 1 1-.25 11.4 11.4 0 0 0 3.6.57 1 1 0 0 1 1 1V20a1 1 0 0 1-1 1A17 17 0 0 1 3 4a1 1 0 0 1 1-1h3.5a1 1 0 0 1 1 1c0 1.25.2 2.45.57 3.57a1 1 0 0 1-.25 1z"/></svg>555-014-2290</span>
    <span><svg width="12" height="10" viewBox="0 0 24 18"><rect x="1" y="1" width="22" height="16" fill="none" stroke="#fff" stroke-width="2"/><path d="M1 1l11 9 11-9" fill="none" stroke="#fff" stroke-width="2"/></svg>contact.us@vantomer.com</span>
  </div>
  <nav class="main-nav abs">
    <a class="active" href="#">HOME</a><a href="#">ABOUT US</a><a href="#">SERVICES ▾</a><a href="#">CONTACT US</a>
  </nav>
</header>

<section class="hero abs" role="img" aria-label="Photo of lab scientists working together with test tubes and equipment">
  <div class="hero-copy abs">
    <h1 class="hero-title">Specializes in offering contract professionals</h1>
    <p class="hero-text">We look for the top people and companies to work with. Whether you are looking for a position, or looking for a contractor, you have come to the right place.</p>
    <div class="hero-actions"><a class="btn" href="#">LEARN MORE</a><a class="btn teal" href="#">SIGN UP</a></div>
  </div>
</section>
<svg class="hero-notch abs" viewBox="0 0 120 46"><path d="M0 46 L60 0 L120 46Z" fill="#eeeeee"/><path d="M50 18l10 10 10-10" fill="none" stroke="#777" stroke-width="3"/></svg>

<section class="clients abs">
  <div class="client-row abs">
    <span class="client-badge"></span>
    <span class="client-name">Halden &amp; Rowe</span>
    <span class="client-name">KORVA</span>
    <span class="client-name">NSTELL</span>
    <span class="client-name">Brambury</span>
    <span class="client-name">LOXTEN</span>
    <span class="client-badge"></span>
  </div>
  <div class="clients-tab abs">OUR CLIENTS</div>
</section>

<h2 class="section-title abs" style="top:770px">Services Offered</h2>
<p class="section-lede abs" style="top:848px">Vantomer specializes in offering contract professionals primarily to companies in pharmaceutical lab environments. We look for the top people and companies to work with, whether you are looking for a position or looking for a contractor, you have come to the right place. We work hard to put great team members together with great teams.</p>

<article class="service abs" style="left:98px">
  <div class="service-photo" role="img" aria-label="Photo of a modern office building with trees" style="background:linear-gradient(#b9cde0,#8d7a63 60%,#6f8a4e)"></div>
  <h3 class="service-title">Client companies</h3>
  <p class="service-text">Vantomer offers professional project managers that can work remotely or onsite. They can be contract, contract to hire, or temporary workers.</p>
</article>
<article class="service abs" style="left:434px">
  <div class="service-photo" role="img" aria-label="Photo of a business team meeting around a laptop" style="background:linear-gradient(120deg,#dbe3ea,#8ea7bb 50%,#5d6f80)"></div>
  <h3 class="service-title">Employee management</h3>
  <p class="service-text">Vantomer offers contract services so your company only has to pay Vantomer for services from our independent contractors.</p>
</article>
<article class="service abs" style="left:771px">
  <div class="service-photo" role="img" aria-label="Photo of a smiling support agent wearing a headset" style="background:linear-gradient(120deg,#cfd4d8,#9aa3ab 55%,#5e6870)"></div>
  <h3 class="service-title">Seeking positions</h3>
  <p class="service-text">Vantomer is focused on contractors for enhancing teams, but we also work in contract for hire, temporary, and permanent positions as well.</p>
</article>

<section class="updates abs">
  <h2 class="section-title abs" style="top:36px;text-transform:lowercase">our latest updates</h2>
  <p class="updates-sub abs" style="top:110px">Vantomer specializes in offering contract professionals<br>See all our latest updates . . .</p>
  <div class="update-lead abs">
    <div class="update-tag">Project Management</div>
    <p class="update-big">Vantomer has a vast network of laboratory and laboratory contacts to find your next flexible team member for your lab from Lab Technicians to Lab Management.</p>
  </div>
  <div class="update-rule abs"></div>
  <div class="update-body abs">
    <p class="intro">But I must explain to you how all this mistaken idea of denouncing pleasure and praising pain was born and I will give you a complete account of the system, and expound the actual teachings of the great explorer of the truth.</p>
    <p>Quis autem vel eum iure reprehenderit qui in ea voluptate velit esse quam nihil molestiae consequatur, vel illum qui dolorem eum fugiat quo voluptas nulla pariatur.</p>
    <p>Sed ut perspiciatis unde omnis iste natus error sit voluptatem accusantium doloremque laudantium, totam rem aperiam, eaque ipsa quae ab illo inventore veritatis et quasi architecto beatae vitae dicta sunt explicabo. Nemo enim ipsam voluptatem quia voluptas sit aspernatur aut odit aut fugit, sed quia consequuntur magni dolores eos qui ratione voluptatem sequi nesciunt.</p>
  </div>
  <svg class="arrow abs" style="left:118px" width="18" height="30" viewBox="0 0 18 30"><path d="M15 2L3 15l12 13" fill="none" stroke="#777" stroke-width="3"/></svg>
  <svg class="arrow abs" style="left:1064px" width="18" height="30" viewBox="0 0 18 30"><path d="M3 2l12 13L3 28" fill="none" stroke="var(--teal)" stroke-width="3"/></svg>
</section>

<h2 class="section-title abs" style="top:1905px">let us know</h2>
<p class="updates-sub abs" style="top:1976px;color:#888">E-mail or say how we can help you.<br>We look forward to hearing from you :)</p>

<div class="quote-mark abs">“</div>
<blockquote class="quote abs">Sed ut perspiciatis unde omnis iste natus error sit voluptatem accusantium doloremque laudantium, totam rem aperiam, eaque ipsa quae ab illo inventore veritatis<span class="quote-cite">- Clara Whitfield -</span></blockquote>
<div class="pitch abs">
  <h3>Let yourself be persuaded to go on a trip</h3>
  <h4>Let's create an interesting project together!</h4>
  <p><b>Get to know us, let us know how you feel.</b> We love meeting new people, listening to their stories, starting new projects and concepts. That's what pushes us to work. Tell us - where you are now and where you would like to be? Do you want to create a great project? Share your ideas... E-mail or call us.</p>
</div>

<div class="divider abs"></div>
<div class="contact-item abs" style="left:330px">Call us<strong>555-014-2290</strong></div>
<div class="contact-brand abs"><span class="brand-dot"></span><span class="brand-name">VANTOMER</span></div>
<div class="contact-item abs" style="left:830px">e-mail<strong>contact.us@vantomer.com</strong></div>

<div class="map abs" role="img" aria-label="Map showing the office location"></div>
<div class="map-card abs">
  <h5>VANTOMER</h5>
  1280 Alder Grove Road,<br>Linwood, CA 90471<br><br>Contact<br>555-014-2290<br>contact.us@vantomer.com
</div>

<footer class="site-footer abs">© 2014-2020 Vantomer<br>Vantomer with enhancing your team</footer>
<div class="footer-band abs"></div>
<a class="to-top abs" href="#" aria-label="Back to top"><svg width="26" height="16" viewBox="0 0 26 16"><path d="M3 13L13 3l10 10" fill="none" stroke="#fff" stroke-width="3"/></svg></a>

</body>
</html>
```